Detox Poster Design Project

I am a naturopath that works in Melbourne. I require a poster that I can put up in my natural therapies clinic that is advertising a detox program that I am offering. The program runs for 3 or 6 weeks and is designed to help your liver, gut and kidney cleanse toxins more efficiently, leaving you feeling energised and healthy.

I would like to see designs that are fresh, organic, clear and contemporary to look at. I want to sell the idea of feeling good, wellbeing and vitality to the potential client. Colours I like include greens, greys and blues.

The final design should communicate health and happiness.

Requirements
Must have
• Please include the photo of the woman in nature.Poster size will be A2 594mm by 420mm
Nice to have
• I have attached the design work for my business cards that you can use. It would be great if the colours and style are in keeping with the existing design work for my business. I have also attached an extra image (almond milk photo) just in case you could see a use for it.

Many thanks.
Should not have
• No hippy, new age looking design.

```html
<!DOCTYPE html>
<html lang="en">
<head>
<meta charset="utf-8">
<title>Sensible Detox Time – Clara Bennett Naturopath</title>
<link rel="stylesheet" href="https://fonts.googleapis.com/css2?family=Roboto+Condensed:wght@700&family=Raleway:wght@300&family=Crimson+Text:ital@1&family=Cinzel:wght@400&family=PT+Sans+Narrow:wght@700&display=swap">
<style>
  :root {
    --brand-blue: #1a72bb;
    --brand-green: #8dc63f;
    --brand-cyan: #22aee0;
    --ink-dark: #3a3a3a;
    --paper: #ffffff;
    --rule: rgba(255,255,255,0.55);
  }
  * { margin: 0; padding: 0; box-sizing: border-box; }
  html, body { width: 1200px; height: 866px; overflow: hidden; background: var(--paper); }
  .poster { position: relative; width: 1200px; height: 866px; overflow: hidden; background: var(--paper); }
  .poster-shapes { position: absolute; inset: 0; }

  .brand { position: absolute; left: 150px; top: 86px; display: flex; align-items: center; gap: 28px; }
  .brand-dot { width: 96px; height: 96px; border-radius: 50%; background: var(--brand-cyan); }
  .brand-name { font-family: 'Raleway', sans-serif; font-weight: 300; color: var(--brand-cyan); line-height: 1.05; white-space: nowrap; }
  .brand-name .brand-person { display: block; font-size: 58px; }
  .brand-name .brand-role { display: block; font-size: 38px; letter-spacing: 0.5px; }

  .photo {
    position: absolute; left: 0; top: 450px; width: 389px; height: 416px;
    background: linear-gradient(160deg, #c98f6c 0%, #e9d4c4 45%, #9cc25a 75%, #e98a2a 100%);
    clip-path: polygon(0 0, 225px 0, 225px 205px, 389px 205px, 389px 416px, 0 416px);
  }

  .headline { position: absolute; left: 157px; width: 480px; top: 258px; text-align: center; font-family: 'Roboto Condensed', sans-serif; font-weight: 700; white-space: nowrap; z-index: 2; }
  .headline-lead { display: block; font-size: 74px; line-height: 74px; color: var(--ink-dark); }
  .headline-main { display: block; font-size: 88px; line-height: 88px; color: var(--brand-blue); margin-top: 6px; letter-spacing: 0.5px; }

  .promise { position: absolute; left: 222px; width: 350px; top: 455px; text-align: center; white-space: nowrap; z-index: 2; }
  .promise-text { font-family: 'PT Sans Narrow', sans-serif; font-weight: 700; font-size: 30px; color: var(--ink-dark); line-height: 44px; }
  .promise-benefit { margin-top: 8px; font-family: 'Roboto Condensed', sans-serif; font-weight: 700; font-size: 40px; line-height: 52px; color: var(--brand-green); }

  .offer { position: absolute; right: 42px; top: 62px; text-align: right; font-family: 'Crimson Text', serif; font-style: italic; color: var(--paper); font-size: 37px; line-height: 50px; }
  .offer .offer-caps { text-transform: uppercase; letter-spacing: 1px; }
  .offer .offer-end { font-size: 56px; line-height: 56px; }

  .question { position: absolute; right: 42px; top: 432px; text-align: right; font-family: 'Cinzel', serif; color: var(--paper); font-size: 38px; line-height: 52px; white-space: nowrap; }

  .contact { position: absolute; right: 42px; top: 634px; width: 462px; color: var(--paper); }
  .contact-intro { font-family: 'Crimson Text', serif; font-style: italic; font-size: 25px; padding-bottom: 6px; border-bottom: 1px solid var(--rule); text-align: right; }
  .contact-phone { font-family: 'PT Sans Narrow', sans-serif; font-weight: 700; font-size: 30px; margin-top: 10px; white-space: nowrap; }
  .contact-phone strong { font-size: 46px; margin-left: 4px; }
  .contact-email { font-family: 'PT Sans Narrow', sans-serif; font-weight: 700; font-size: 24px; padding-bottom: 10px; border-bottom: 1px solid var(--rule); white-space: nowrap; }
  .contact-credit { font-family: 'Crimson Text', serif; font-style: italic; font-size: 22px; margin-top: 8px; white-space: nowrap; }
  .contact-credit small { font-size: 16px; }
</style>
</head>
<body>
<main class="poster">
  <svg class="poster-shapes" width="1200" height="866" viewBox="0 0 1200 866" aria-hidden="true">
    <path d="M0 0 L108 0 C45 150 26 320 24 866 L0 866 Z" fill="var(--brand-blue)"/>
    <path d="M36 300 C28 380 26 430 28 500" fill="none" stroke="var(--brand-green)" stroke-width="4"/>
    <path d="M940 0 L972 0 C760 260 600 560 548 866 L538 866 C585 560 735 260 940 0 Z" fill="var(--brand-green)"/>
    <path d="M992 0 L1200 0 L1200 866 L566 866 C620 560 780 260 992 0 Z" fill="var(--brand-blue)"/>
  </svg>

  <div class="brand">
    <span class="brand-dot"></span>
    <p class="brand-name"><span class="brand-person">Clara Bennett</span><span class="brand-role">NATUROPATH</span></p>
  </div>

  <div class="photo" role="img" aria-label="Smiling woman beside a bowl of fresh fruit, vegetables and a glass of orange juice"></div>

  <h1 class="headline"><span class="headline-lead">It’s Sensible</span><span class="headline-main">DETOX TIME</span></h1>

  <div class="promise">
    <p class="promise-text">Press Reset on<br>Your Bad Eating Habits to</p>
    <p class="promise-benefit">FEEL ENERGISED<br>&amp; VITAL</p>
  </div>

  <p class="offer">Have a<br><span class="offer-caps">Detox</span><br><span class="offer-caps">Program</span><br>tailored<br><span class="offer-end">for you</span></p>

  <p class="question">Overindulge<br>over the holidays?</p>

  <div class="contact">
    <p class="contact-intro">For more information contact</p>
    <p class="contact-phone">Call us TODAY - <strong>0400 318 462</strong></p>
    <p class="contact-email">email: info@thebalancednaturopath.com</p>
    <p class="contact-credit">Clara Bennett - <small>B.A., B.H.Sc. (Naturopathy), Member NTPA</small></p>
  </div>
</main>
</body>
</html>
```